Packaging Design: Logo/Bottle Design for New Botanical Cocktail Brand

We are a new start up, looking to create a new line of Ready to drink Cocktails. The brand name is Verdelle Garden Cocktails, infused with fruit, herb, and floral botanicals grown on our farm in New Hampshire. Flavors will include: Herb flavored with cilantro, Berry- flavored with Alpine Strawberry, Citrus flavored with lemon Verbena & lemon balm, Pear flavored with Bartlett pear, Cucumber & Mint. We need a logo and a label design. There are 2 possible bottles to choose from.

Designer has complete freedom with everything! From fonts and colors to bottle caps and closures. Please view the pinterest link for inspirational bottle designs. https://www.pinboardly.example/kestrawynn/garden-drinks/

Target Market(s)

Female 21 to 48 years old. College educated and professional. The type of person that has a passion for a cause and eats and shops local. People that respect an artisan quality product, hand made by a master craftsman.

Industry/Entity Type

Floral

Requirements
Must have
• Clear Bottle, see options attached. You may also choose your own BUT WE MUST SEE THE LOGO AND IMAGERY ON A BOTTLE
• Logo Design: "Verdelle Garden Cocktails"
• Label: We can have front and back, or one continuous label. We are open to painted designs.
• The label must contain the following text in quotes:
• Product Name: " Verdelle Garden Cocktails "
• "15% Alc. by Vol. (30 proof)"
• "750 mL"
• "Handcrafted and Bottled by Harrow Creek Orchard Farm and Distillery
• Winchester, NH-USA"
• The following Text must be in all caps and 3mm in height:
• "Government Warning: (1) According to the Surgeon General, women should not drink alcoholic beverages during pregnancy because of the risk of birth defects. (2) Consumption of alcoholic beverages impairs your ability to drive a car or operate machinery and may cause health problems."
• Must be a space for a bar code: .75 in height by 1.25 in length.
• “www.harrowcreekorchard.example”
• Must Have the following Statement:
• Infused with fruit, herb, and floral botanicals and sweetened with stevia. Serve cold over ice.
Nice to have
• Antique or vintage botanical illustrations
• https://www.pinboardly.example/kestrawynn/garden-drinks/
• check out the board for inspiration.
• Think artisanal small batch spirits that are ready to drink out of the bottle. Refreshing flavors just pour over ice and add herb leaves.
• You can use images by doing a search here.
• http://archive.plantrecords.example/search.xhtml?start=0&collectionFacet=Orchard+Fruit+Painting+Set

```html
<!DOCTYPE html>
<html lang="en">
<head>
<meta charset="utf-8">
<title>Verdelle Garden Cocktails – Citrus Label</title>
<link rel="stylesheet" href="https://fonts.googleapis.com/css2?family=Pinyon+Script&family=Oswald:wght@400;600&display=swap">
<style>
  :root {
    --page-bg: #ffffff;
    --lime: #c9dc2c;
    --lime-deep: #bfd424;
    --parchment: #e9dcc0;
    --leaf: #8fa07a;
    --fruit: #c9cf8a;
    --ink: #2a2a22;
    --ink-soft: #3a3a30;
  }
  * { margin: 0; padding: 0; box-sizing: border-box; }
  html, body {
    width: 1200px;
    height: 1000px;
    overflow: hidden;
    background: var(--page-bg);
  }
  .canvas {
    position: relative;
    width: 1200px;
    height: 1000px;
  }
  .label {
    position: absolute;
    left: 420px;
    top: 35px;
    width: 360px;
    height: 930px;
    display: flex;
    box-shadow: 0 2px 10px rgba(0,0,0,0.08);
  }
  .label__botanical {
    width: 62px;
    height: 100%;
    background:
      radial-gradient(circle at 50% 12%, var(--fruit) 0 18%, transparent 30%),
      radial-gradient(circle at 40% 55%, var(--leaf) 0 14%, transparent 32%),
      radial-gradient(circle at 55% 88%, var(--fruit) 0 16%, transparent 30%),
      linear-gradient(180deg, var(--parchment), #e2d4b4 50%, var(--parchment));
  }
  .label__band {
    flex: 1;
    height: 100%;
    background: linear-gradient(90deg, var(--lime-deep), var(--lime) 20%, var(--lime) 80%, var(--lime-deep));
    display: flex;
    flex-direction: column;
    align-items: center;
    color: var(--ink);
    text-align: center;
    padding: 0 22px;
  }
  .brand {
    margin-top: 100px;
    font-family: "Pinyon Script", cursive;
    color: var(--ink);
    line-height: 1;
  }
  .brand__name {
    display: block;
    font-size: 44px;
  }
  .brand__tagline {
    display: block;
    font-size: 20px;
    margin-top: 2px;
    padding-left: 60px;
  }
  .statement {
    margin-top: 80px;
    font-family: "Pinyon Script", cursive;
    font-size: 23px;
    line-height: 1.45;
    color: var(--ink-soft);
  }
  .flavor {
    margin-top: 110px;
    font-family: "Oswald", sans-serif;
    font-weight: 600;
    font-size: 46px;
    letter-spacing: 1px;
    line-height: 1;
  }
  .flavor__note {
    margin-top: 6px;
    font-family: "Oswald", sans-serif;
    font-weight: 400;
    font-size: 14px;
    line-height: 1.25;
    text-transform: uppercase;
    text-align: left;
    align-self: stretch;
    padding-left: 16px;
  }
  .specs {
    margin-top: auto;
    margin-bottom: 34px;
    font-family: "Oswald", sans-serif;
    font-weight: 400;
    line-height: 1.3;
  }
  .specs__abv { display: block; font-size: 13px; }
  .specs__volume { display: block; font-size: 17px; }
</style>
</head>
<body>
  <main class="canvas">
    <section class="label">
      <div class="label__botanical label__botanical--left" role="img" aria-label="Vintage botanical illustration of lemons, leaves and blossoms"></div>
      <div class="label__band">
        <h1 class="brand">
          <span class="brand__name">Verdelle</span>
          <span class="brand__tagline">Garden Cocktails</span>
        </h1>
        <p class="statement">Infused with fruit,<br>herb, and floral<br>botanicals and<br>sweetened with stevia.<br>Serve cold over ice.</p>
        <h2 class="flavor">CITRUS</h2>
        <p class="flavor__note">Flavored with lemon verbena &amp;<br>lemon balm</p>
        <p class="specs">
          <span class="specs__abv">15% Alc. by Vol. (30 proof)</span>
          <span class="specs__volume">750 mL</span>
        </p>
      </div>
      <div class="label__botanical label__botanical--right" role="img" aria-label="Vintage botanical illustration of lemons, leaves and blossoms"></div>
    </section>
  </main>
</body>
</html>
```